Need a business card for my new home staging and redesign business. Business name: Quillamore Interiors. Subtitle: Thoughtful Styling for Homes That Sell

Target Market(s)

Realtors, home sellers

Industry/Entity Type

Real Estate

Contact Information for Business Card

I don't have a website address yet, or a business Facebook account, but would like to include those. Do not have a logo or any graphics

Font styles to use
Sans Serif

Colors

Designer to choose colors to be used in the design.

Requirements
Must have
• Placeholders for contact details, e.g. Phone, email, web address, etc.
Nice to have
• Sophisticated but somewhat whimsical feel. Perhaps a stylized star (or magic wand?) over the "I" in interiors to convey inspiration.
Should not have
• Nothing too cutesy, including cartoon wizards.

```html
<!DOCTYPE html>
<html lang="en">
<head>
<meta charset="utf-8">
<title>Quillamore Interiors – Business Card</title>
<link rel="stylesheet" href="https://fonts.googleapis.com/css2?family=Lato:wght@400;700&display=swap">
<style>
  :root {
    --navy: #0f4774;
    --lime: #8dc21f;
    --white: #ffffff;
    --backdrop: #ece9e6;
  }
  * { margin: 0; padding: 0; box-sizing: border-box; }
  html, body {
    width: 1200px; height: 900px; overflow: hidden;
    background: var(--backdrop);
    font-family: "Lato", sans-serif;
  }
  .canvas { position: relative; width: 1200px; height: 900px; }

  .card { position: absolute; overflow: hidden; box-shadow: 0 6px 18px rgba(0,0,0,0.15); }

  /* Contact side */
  .card-contact {
    left: 178px; top: 74px; width: 588px; height: 364px;
    background: var(--navy);
  }
  .card-contact .accent-panel { position: absolute; left: 0; top: 0; width: 588px; height: 364px; }
  .contact-block {
    position: absolute; right: 36px; top: 140px;
    text-align: right; color: var(--white);
  }
  .person-name { font-size: 21px; font-weight: 700; letter-spacing: 0.5px; line-height: 26px; }
  .person-role { font-size: 17px; font-weight: 400; line-height: 20px; }
  .contact-list { list-style: none; margin-top: 14px; }
  .contact-list li {
    font-size: 16px; line-height: 22px;
    display: flex; justify-content: flex-end; align-items: center; gap: 4px;
  }
  .contact-list svg { width: 13px; height: 13px; fill: var(--white); }
  .social-row {
    position: absolute; left: 315px; right: 36px; top: 288px;
    display: flex; align-items: center; gap: 8px;
  }
  .social-row .rule { flex: 1; height: 1px; background: rgba(255,255,255,0.45); }
  .social-dot { width: 26px; height: 26px; border-radius: 50%; background: var(--white); }

  /* Brand side */
  .card-brand {
    left: 388px; top: 505px; width: 566px; height: 352px;
    background: var(--white);
  }
  .brand-mark {
    position: absolute; left: 0; right: 0; top: 110px;
    display: flex; flex-direction: column; align-items: center;
  }
  .brand-dot { width: 30px; height: 30px; border-radius: 50%; background: var(--lime); margin-bottom: 40px; }
  .brand-name {
    font-size: 33px; font-weight: 400; color: var(--navy);
    letter-spacing: 1px; line-height: 38px; text-align: center; text-transform: uppercase;
  }
  .tagline-band {
    position: absolute; left: 0; right: 0; bottom: 0; height: 57px;
    background: var(--navy); color: var(--white);
    display: flex; align-items: center; justify-content: center;
    font-size: 15px; font-weight: 700; letter-spacing: 0.3px; text-transform: uppercase;
  }
</style>
</head>
<body>
<main class="canvas">

  <section class="card card-contact">
    <svg class="accent-panel" viewBox="0 0 588 364" aria-hidden="true">
      <polygon points="0,0 174,0 0,360" fill="var(--lime)"/>
    </svg>
    <div class="contact-block">
      <p class="person-name">DANIEL HARTLEY</p>
      <p class="person-role">Managing Director</p>
      <ul class="contact-list">
        <li>444 555 2190
          <svg viewBox="0 0 16 16" aria-hidden="true"><path d="M2 5c0-2 2-3 6-3s6 1 6 3v1h-3V5H5v1H2zM4 7h8l2 6H2z"/></svg>
        </li>
        <li>hello@quillamore.com
          <svg viewBox="0 0 16 16" aria-hidden="true"><path d="M1 3h14v10H1zM2 4l6 5 6-5z" fill-rule="evenodd"/></svg>
        </li>
        <li>www.quillamore.com
          <svg viewBox="0 0 16 16" aria-hidden="true"><circle cx="8" cy="8" r="7"/></svg>
        </li>
      </ul>
    </div>
    <div class="social-row">
      <span class="rule"></span>
      <span class="social-dot" aria-label="Social profile"></span>
      <span class="social-dot" aria-label="Social profile"></span>
    </div>
  </section>

  <section class="card card-brand">
    <div class="brand-mark">
      <span class="brand-dot" aria-hidden="true"></span>
      <p class="brand-name">Quillamore<br>Interiors</p>
    </div>
    <div class="tagline-band">Thoughtful Styling for Homes That Sell</div>
  </section>

</main>
</body>
</html>
```